Social Media Graphics - Harbor Climb REVISED

Create 6-7 individual social media graphics (square size) to encourage folks to join our online course called:

The Lantern Ledger Plan
How to Launch a Multi-Million Business From Scratch
Sign Up Today!

IMPORTANT: Make the largest and most prominent text on the graphic be: How to Launch a Multi-Million Business From Scratch

For the color scheme of the graphics, let's try a blue color palette; make sure the graphics appeal to both men and women

Make sure each graphic contains 1 of the 3 pics attached (crop pic as needed); and make sure one of the graphics is all TEXT only.

Target Market(s)

men and women looking to start a business

Industry/Entity Type

Entrepreneurship

Colors
0054AA
0677BA
7BADD7
CADEEF
E8F1F8

Requirements
Must have
• All the text and use the 3 pics provided; one graphic can be all text; Simple, modern design that's easy to read

```html
<!DOCTYPE html>
<html lang="en">
<head>
<meta charset="utf-8">
<title>The Lantern Ledger Plan – Sign Up</title>
<link href="https://fonts.googleapis.com/css2?family=Montserrat:wght@700;800;900&display=swap" rel="stylesheet">
<style>
  :root {
    --page: #ffffff;
    --navy: #063b6e;
    --glow: #7badd7;
    --glow-soft: #2f66a6;
    --frame: #ffffff;
    --headline: #eef20c;
    --button: #1cb2ef;
    --button-ink: #0b1f86;
  }
  * { margin: 0; padding: 0; box-sizing: border-box; }
  html, body {
    width: 1200px; height: 1200px; overflow: hidden;
    background: var(--page);
    font-family: "Montserrat", "Century Gothic", sans-serif;
  }
  .canvas { position: relative; width: 1200px; height: 1200px; }
  .panel {
    position: absolute; left: 178px; top: 162px;
    width: 849px; height: 848px;
    background: var(--navy);
    overflow: hidden;
  }
  .frame { position: absolute; left: 0; top: 0; }
  .course-title {
    position: absolute; left: 0; right: 0; top: 48px;
    text-align: center; color: var(--frame);
    text-shadow: 0 2px 6px rgba(0,0,0,0.35);
  }
  .course-title .kicker {
    display: block; font-size: 38px; font-weight: 800; letter-spacing: 2px; line-height: 44px;
  }
  .course-title .main {
    display: block; font-size: 66px; font-weight: 800; letter-spacing: 2px; line-height: 72px;
  }
  .host-photo {
    position: absolute; left: 90px; top: 150px;
    width: 670px; height: 420px;
    background: radial-gradient(ellipse 48% 58% at 50% 40%, var(--glow) 0%, var(--glow-soft) 55%, rgba(6,59,110,0) 100%);
  }
  .headline {
    position: absolute; left: 0; right: 0; top: 486px;
    text-align: center; color: var(--headline);
    font-size: 54px; font-weight: 800; line-height: 48px; letter-spacing: 1px;
    text-transform: uppercase;
    text-shadow: 0 3px 6px rgba(0,0,0,0.45);
  }
  .cta {
    position: absolute; left: 325px; top: 660px;
    width: 198px; height: 146px; border-radius: 50%;
    background: var(--button);
    border: 5px solid var(--frame);
    display: flex; flex-direction: column; align-items: center; justify-content: center;
    color: var(--button-ink); font-weight: 900; line-height: 1;
    -webkit-text-stroke: 1px var(--frame);
    paint-order: stroke fill;
  }
  .cta .line-1 { font-size: 27px; }
  .cta .line-2 { font-size: 36px; margin-top: 2px; }
</style>
</head>
<body>
<div class="canvas">
  <div class="panel">
    <div class="host-photo" role="img" aria-label="Photo of the two course hosts, a man in a black turtleneck and a woman in a denim jacket, smiling against a light blue glow"></div>
    <svg class="frame" width="849" height="848" viewBox="0 0 849 848" aria-hidden="true">
      <g stroke="var(--frame)" stroke-width="2" fill="none">
        <line x1="90" y1="70" x2="252" y2="70"/>
        <line x1="585" y1="70" x2="758" y2="70"/>
        <line x1="90" y1="70" x2="90" y2="485"/>
        <line x1="90" y1="600" x2="90" y2="741"/>
        <line x1="758" y1="70" x2="758" y2="485"/>
        <line x1="758" y1="600" x2="758" y2="741"/>
        <line x1="90" y1="741" x2="325" y2="741"/>
        <line x1="523" y1="741" x2="758" y2="741"/>
      </g>
    </svg>
    <h1 class="course-title">
      <span class="kicker">THE LANTERN</span>
      <span class="main">LEDGER PLAN</span>
    </h1>
    <h2 class="headline">How to Launch a<br>Multi-Million Business<br>From Scratch</h2>
    <div class="cta">
      <span class="line-1">SIGN UP</span>
      <span class="line-2">TODAY!</span>
    </div>
  </div>
</div>
</body>
</html>
```